Tarrow Creek plumbing plumbing company business card design

Something sinilar to business card i upload it is my old business card design
And have a good watermark with the logo or majority of the logot in rhe background as watermark

Plumbing business similar to uploaded design with a nice watermark of the logo

Font styles to use
Script

Colors

Designer to choose colors to be used in the design.

```html
<!DOCTYPE html>
<html lang="en">
<head>
<meta charset="utf-8">
<title>Tarrow Creek Plumbing – Business Card</title>
<link rel="stylesheet" href="https://fonts.googleapis.com/css2?family=Montserrat:wght@300;400;500;700;800&display=swap">
<style>
  :root {
    --backdrop: #2b2e33;
    --card-white: #f4f5f7;
    --brand-blue: #0b78c1;
    --ink: #1c1c1e;
    --ink-soft: #3a3b3f;
    --wash: #dde7f1;
  }
  * { box-sizing: border-box; margin: 0; padding: 0; }
  html, body {
    width: 1200px; height: 900px; overflow: hidden;
    background: var(--backdrop);
    font-family: "Montserrat", sans-serif;
  }
  .stage {
    position: relative; width: 1200px; height: 900px;
    display: flex; align-items: center; justify-content: center; gap: 48px;
  }
  .card {
    position: relative; width: 525px; height: 300px; overflow: hidden;
    box-shadow: 0 18px 40px rgba(0,0,0,.45);
  }

  /* front */
  .card--front { background: var(--card-white); color: var(--ink); }
  .watermark {
    position: absolute; left: 120px; top: 70px; width: 250px; height: 250px;
    border-radius: 50% 50% 50% 8%;
    transform: rotate(-45deg);
    background: radial-gradient(circle at 50% 50%, rgba(221,231,241,.35) 0 35%, var(--wash) 60%, rgba(221,231,241,.5) 100%);
  }
  .card__divider { position: absolute; left: 252px; width: 7px; background: var(--brand-blue); }
  .card__divider--top { top: 0; height: 90px; }
  .card__divider--bottom { bottom: 0; height: 80px; }

  .wordmark {
    position: absolute; left: 34px; top: 72px;
    display: flex; align-items: center; gap: 9px;
  }
  .wordmark__dot { width: 26px; height: 26px; border-radius: 50%; background: var(--brand-blue); flex: none; }
  .wordmark__name {
    font-weight: 800; font-size: 17px; line-height: 1.12; color: var(--ink); width: 150px;
  }
  .brand-rule { position: absolute; left: 40px; top: 138px; width: 52px; height: 2px; background: var(--brand-blue); }
  .licence { position: absolute; left: 40px; top: 158px; font-size: 13px; font-weight: 400; color: var(--ink-soft); }

  .contact {
    position: absolute; left: 278px; top: 150px; list-style: none;
    font-size: 11px; color: var(--ink-soft);
  }
  .contact li { display: flex; align-items: center; gap: 8px; margin-bottom: 9px; }
  .contact svg { width: 15px; height: 15px; flex: none; }

  .person {
    position: absolute; right: 34px; top: 50px; text-align: right;
    padding-right: 10px; border-right: 3px solid var(--brand-blue);
  }
  .person__name { font-weight: 700; font-size: 16px; letter-spacing: .5px; text-transform: uppercase; }
  .person__role { font-size: 17px; font-weight: 300; color: var(--ink-soft); }

  /* back */
  .card--back {
    background: var(--brand-blue); color: #fff;
    display: flex; flex-direction: column; align-items: center; justify-content: center;
  }
  .back__mark { display: flex; align-items: center; gap: 12px; }
  .back__dot { width: 36px; height: 36px; border-radius: 50%; background: #fff; }
  .back__name { font-weight: 800; font-size: 28px; color: #fff; }
  .back__rule { width: 60px; height: 2px; background: #fff; margin: 26px 0 22px; }
  .back__web { font-size: 16px; font-weight: 300; letter-spacing: .4px; }
</style>
</head>
<body>
<main class="stage">
  <section class="card card--front">
    <div class="watermark" role="img" aria-label="Faint pale-blue logo watermark"></div>
    <span class="card__divider card__divider--top"></span>
    <span class="card__divider card__divider--bottom"></span>

    <div class="wordmark">
      <span class="wordmark__dot"></span>
      <p class="wordmark__name">Tarrow Creek plumbing</p>
    </div>
    <span class="brand-rule"></span>
    <p class="licence">Lic No. 480726C</p>

    <ul class="contact">
      <li>
        <svg viewBox="0 0 16 16"><rect width="16" height="16" rx="3" fill="var(--brand-blue)"/><path d="M5 4l2 2-1 1.2a6 6 0 003 3L10.2 9l2 2-1.3 1.3C8 12 4 8 3.7 5.2z" fill="#fff"/></svg>
        0412-555-190
      </li>
      <li>
        <svg viewBox="0 0 16 16"><rect width="16" height="16" rx="3" fill="var(--brand-blue)"/><circle cx="8" cy="8" r="4.5" fill="none" stroke="#fff"/><path d="M3.5 8h9M8 3.5c-2 2.5-2 6.5 0 9M8 3.5c2 2.5 2 6.5 0 9" fill="none" stroke="#fff" stroke-width=".8"/></svg>
        tarrowcreekplumbing.com.au
      </li>
      <li>
        <svg viewBox="0 0 16 16"><rect width="16" height="16" rx="3" fill="var(--brand-blue)"/><rect x="3.5" y="5" width="9" height="6.5" fill="none" stroke="#fff"/><path d="M3.5 5l4.5 3.5L12.5 5" fill="none" stroke="#fff"/></svg>
        info@tarrowcreekplumbing.com
      </li>
    </ul>

    <div class="person">
      <p class="person__name">Darren Holloway</p>
      <p class="person__role">Director</p>
    </div>
  </section>

  <section class="card card--back">
    <div class="back__mark">
      <span class="back__dot"></span>
      <p class="back__name">Tarrow Creek plumbing</p>
    </div>
    <span class="back__rule"></span>
    <p class="back__web">tarrowcreekplumbing.com.au</p>
  </section>
</main>
</body>
</html>
```